"Every Lantern Still Burning" Sermon Series Design

Needing a design for our church's next sermon series titled "Every Lantern Still Burning" where we will discuss the need for unity, diversity, love and clarity. Looking for a 1920 x 1080 (or higher res) editable and layered file (PSD or AI) so that we can reformat the design to work on social, screens, lower thirds and various print and online mediums. We will also need to have access to the font files so that we can make resize and tweak as needed. We like the idea of using a globe or map of the world as the backdrop with the words overtop. Or, the idea of creating a bunch of newspaper clippings (generic, so that they can't actually be read) and making the shape of a heart. See attached examples. This website will give you an idea of our previous sermon series designs so you can have an idea of our style (but, feel free to help us advance the ball on something more aligned with current design trends): https://www.brinmoorfellowship.church/series

Examples use red, but stay away from a ton of red. If you're gonna major in a color, use blue or something in that family.

Must haves:
Title: Every Lantern Still Burning
Tagline : (TBD - use some Lorem Ipsum as a placeholder and we will fill in later)
Our Logo (attached) (small towards bottom is standard - only use solid colors for logo - preferably just solid black or white)

Industry/Entity Type

Church

Font styles to use
Serif
Sans Serif

Requirements
Must have
• Title: Every Lantern Still Burning
Nice to have
• We like the idea of using a globe or map of the world as the backdrop with the words overtop. Or, the idea of creating a bunch of newspaper clippings (generic, so that they can't actually be read) and making the shape of a heart. See attached examples.

If you're gonna major on a color, stick with blue or something close.
Should not have
• Don't use red as the primary color (example we sent has red, but stay away from it)

```html
<!DOCTYPE html>
<html lang="en">
<head>
<meta charset="utf-8">
<title>Every Lantern Still Burning — Sermon Series</title>
<link href="https://fonts.googleapis.com/css2?family=Montserrat:ital,wght@0,300;0,400;0,800;1,400;1,800&display=swap" rel="stylesheet">
<style>
  :root {
    --page-grey: #cbcbcb;
    --navy: #1b2740;
    --navy-deep: #181f33;
    --globe-green: #7dbf53;
    --copper: #d59a78;
    --white: #ffffff;
  }
  * { margin: 0; padding: 0; box-sizing: border-box; }
  html, body {
    width: 1200px; height: 957px; overflow: hidden;
    background: var(--page-grey);
    font-family: "Montserrat", Arial, sans-serif;
  }
  .series-banner {
    position: absolute; left: 63px; top: 160px;
    width: 1069px; height: 605px;
    background: var(--navy); overflow: hidden;
  }
  .banner-art { position: absolute; inset: 0; width: 100%; height: 100%; }
  .series-title {
    position: absolute; left: 0; right: 0; top: 0;
    text-align: center; color: var(--white);
    text-shadow: 2px 4px 6px rgba(0,0,0,.35);
    transform: translateX(-72px);
  }
  .series-title span { display: block; line-height: 1; }
  .title-lead {
    margin-top: 190px; font-weight: 800; font-style: italic;
    font-size: 46px; letter-spacing: 1px;
  }
  .title-main { margin-top: 4px; font-weight: 800; font-size: 104px; letter-spacing: -3px; }
  .title-second { margin-top: 4px; font-weight: 800; font-size: 92px; letter-spacing: -2px; }
  .title-last { margin-top: 8px; font-weight: 300; font-size: 68px; text-shadow: none; }
  .tagline {
    position: absolute; right: 124px; top: 523px;
    color: var(--white); font-size: 15.5px; line-height: 19px;
    text-align: right; font-weight: 400;
  }
  .tagline em { font-weight: 800; font-style: italic; }
  .church-mark {
    position: absolute; right: 20px; top: 512px;
    display: flex; flex-direction: column; align-items: center; gap: 5px;
    color: var(--white); font-size: 11px; font-weight: 400;
    text-align: center; line-height: 13px; width: 84px;
  }
  .church-mark .mark-dot {
    width: 16px; height: 16px; border-radius: 50%;
    border: 2px solid var(--white);
  }
</style>
</head>
<body>
  <main class="series-banner">
    <svg class="banner-art" viewBox="0 0 1069 605" xmlns="http://www.w3.org/2000/svg">
      <defs>
        <linearGradient id="hand-tone" x1="0" y1="0" x2="1" y2="1">
          <stop offset="0" stop-color="#d59a78" stop-opacity=".14"/>
          <stop offset="1" stop-color="#d59a78" stop-opacity=".05"/>
        </linearGradient>
        <radialGradient id="globe-tone" cx=".5" cy=".5" r=".5">
          <stop offset="0" stop-color="#3f6a48"/>
          <stop offset=".75" stop-color="#5f9a4c"/>
          <stop offset="1" stop-color="#7dbf53"/>
        </radialGradient>
      </defs>
      <path class="bg-band-top" fill="var(--navy-deep)" d="M467 0 H1069 V318 C950 270 860 230 790 175 C700 110 560 80 467 0 Z"/>
      <path class="bg-band-bottom" fill="var(--navy-deep)" d="M0 265 C120 255 230 260 280 300 C340 350 360 420 450 440 C560 460 690 480 780 605 H0 Z"/>
      <rect class="upper-hand-illustration" role="img" aria-label="Line drawing of a hand reaching down from the upper right" x="480" y="15" width="589" height="340" rx="60" fill="url(#hand-tone)"/>
      <rect class="lower-hand-illustration" role="img" aria-label="Line drawing of an open hand cradling from the lower left" x="0" y="410" width="590" height="195" rx="50" fill="url(#hand-tone)"/>
      <rect class="leaf-sprig-left" role="img" aria-label="Line-drawn leaf sprigs" x="0" y="5" width="90" height="215" rx="20" fill="url(#hand-tone)"/>
      <rect class="leaf-sprig-left-low" role="img" aria-label="Line-drawn leaves" x="0" y="345" width="105" height="80" rx="20" fill="url(#hand-tone)"/>
      <rect class="leaf-sprig-right" role="img" aria-label="Line-drawn leaf sprigs" x="945" y="20" width="124" height="145" rx="20" fill="url(#hand-tone)"/>
      <rect class="leaf-sprig-right-low" role="img" aria-label="Line-drawn leaf bud" x="1010" y="365" width="59" height="80" rx="16" fill="url(#hand-tone)"/>
      <circle class="globe-illustration" role="img" aria-label="Green world globe with white grid lines" cx="454" cy="305" r="204" fill="url(#globe-tone)" opacity=".85"/>
    </svg>

    <h1 class="series-title">
      <span class="title-lead">Every</span>
      <span class="title-main">Lantern</span>
      <span class="title-second">Still</span>
      <span class="title-last">Burning</span>
    </h1>

    <p class="tagline">Lorem Ipsum is <em>simply dummy</em> text of<br>the printing and typesetting industry.</p>

    <div class="church-mark">
      <span class="mark-dot"></span>
      <span class="mark-name">Brinmoor Fellowship</span>
    </div>
  </main>
</body>
</html>
```